Business card for builder specialising in renovations.

Need a card for our building business. Business name is under Martin Pelloe.
Have licence number on card ( 527916K)
Contact number (0400 382 615)
Want to work on logo for some business cards and shirts - something with MP or MPB or open to ideas??
No animations, No hammers. Something sharp and eye catching.
Highlight that we are a renovation specialist. Simple on front with extra details on back with some lines to jot down things.

Target Market(s)

Renovators

Industry/Entity Type

Building

Contact Information for Business Card

2 sided with room on back to jot things down.
Extra details on back so front can be simple ..like, renovations, bathrooms, decks, extensions, new builds,

Logo Text

MP

Font styles to use
Serif

Requirements
Must have
• Eye catching design .
• Name : Martin pelloe
• Licence number
• Contact number - 0400382615
Nice to have
• Some logo design that we can carry through to other forms of advertising
• Local builder
• Quality work
Should not have
• No animations

```html
<!DOCTYPE html>
<html lang="en">
<head>
<meta charset="utf-8">
<title>Martin Pelloe – Business Card</title>
<link rel="stylesheet" href="https://fonts.googleapis.com/css2?family=Open+Sans:wght@400;600;700&display=swap">
<style>
  :root {
    --brand-blue: #05a1d2;
    --ink-white: #ffffff;
    --card-white: #ffffff;
    --backdrop: #ececec;
    --watermark: #f1f1f1;
    --card-shadow: rgba(0, 0, 0, 0.14);
  }
  * { box-sizing: border-box; margin: 0; padding: 0; }
  html, body {
    width: 1200px;
    height: 900px;
    overflow: hidden;
  }
  body {
    position: relative;
    background: var(--backdrop);
    font-family: "Open Sans", Arial, sans-serif;
  }
  .card {
    position: absolute;
    background: var(--card-white);
    box-shadow: 0 6px 22px var(--card-shadow);
    overflow: hidden;
  }

  /* Front */
  .card--front {
    left: 78px;
    top: 34px;
    width: 587px;
    height: 364px;
  }
  .front__panel {
    position: absolute;
    left: 0;
    top: 0;
    width: 278px;
    height: 100%;
    background: var(--brand-blue);
    color: var(--ink-white);
    text-align: center;
  }
  .front__name {
    position: absolute;
    left: 0;
    right: 0;
    top: 114px;
    font-size: 25px;
    font-weight: 700;
  }
  .front__phone {
    position: absolute;
    left: 0;
    right: 0;
    top: 191px;
    font-size: 17px;
    font-weight: 400;
  }
  .front__licence {
    position: absolute;
    left: 0;
    right: 0;
    top: 224px;
    font-size: 17px;
    font-weight: 400;
  }
  .front__licence-label { font-weight: 600; }
  .front__brand {
    position: absolute;
    left: 278px;
    top: 0;
    width: 309px;
    height: 100%;
  }
  .brand-mark {
    position: absolute;
    left: 104px;
    top: 100px;
    width: 100px;
    height: 100px;
    background: var(--brand-blue);
  }
  .brand-name {
    position: absolute;
    left: 0;
    right: 0;
    top: 214px;
    text-align: center;
    font-size: 40px;
    font-weight: 600;
    line-height: 1.2;
    color: var(--brand-blue);
  }

  /* Back */
  .card--back {
    left: 388px;
    top: 505px;
    width: 567px;
    height: 352px;
  }
  .back__watermark {
    position: absolute;
    left: 0;
    top: 0;
    width: 100%;
    height: 100%;
  }
  .back__band {
    position: absolute;
    left: 0;
    right: 0;
    top: 110px;
    height: 131px;
    background: var(--brand-blue);
    display: flex;
    align-items: center;
    justify-content: center;
  }
  .back__services {
    color: var(--ink-white);
    font-size: 23px;
    font-weight: 600;
    line-height: 1.35;
    text-align: center;
  }
</style>
</head>
<body>
  <section class="card card--front" aria-label="Business card front">
    <div class="front__panel">
      <p class="front__name">Martin Pelloe</p>
      <p class="front__phone">0400 382 615</p>
      <p class="front__licence"><span class="front__licence-label">License No-</span> 527916K</p>
    </div>
    <div class="front__brand">
      <div class="brand-mark" aria-hidden="true"></div>
      <p class="brand-name">Martin Pelloe</p>
    </div>
  </section>

  <section class="card card--back" aria-label="Business card back">
    <svg class="back__watermark" viewBox="0 0 567 352" aria-hidden="true">
      <circle cx="280" cy="176" r="160" fill="var(--watermark)"/>
    </svg>
    <div class="back__band">
      <p class="back__services">Rrenovations, bathrooms, decks,<br>extensions, new builds etc</p>
    </div>
  </section>
</body>
</html>
```